Broadway Haulage website

We need a website design for a towing company based in Australia.
The design should be simple and minimalist. The site can be in colours of the logo are Blue, Red and White (see attached) - but we'd like to see options in some sort of industrial looking metallic theme if possible.
We base our business on our friendly and efficient customer service, the design should attempt to convey this in some way.

Industry/Entity Type

Industrial

Font styles to use
Sans Serif

```html
<!DOCTYPE html>
<html lang="en">
<head>
<meta charset="utf-8">
<title>Broadway Haulage</title>
<link href="https://fonts.googleapis.com/css2?family=Questrial&display=swap" rel="stylesheet">
<style>
  :root {
    --black: #060606;
    --panel-top: #1e1e1e;
    --red: #e31b23;
    --blue: #2f4f9c;
    --navy: #0f2464;
    --white: #ffffff;
    --text-soft: #c9c9c9;
  }
  * { margin: 0; padding: 0; box-sizing: border-box; }
  html, body { width: 1020px; height: 1200px; overflow: hidden; background: var(--black); }
  body { position: relative; font-family: "Questrial", "Century Gothic", sans-serif; color: var(--white); }

  .site-header {
    position: absolute; left: 0; top: 0; width: 1020px; height: 70px;
    background: linear-gradient(#2a2a2a, #0b0b0b);
    z-index: 3;
  }
  .red-band { position: absolute; left: 0; top: 70px; width: 1020px; height: 33px; background: var(--red); z-index: 2; }
  .brand {
    position: absolute; left: 50px; top: 18px; z-index: 4;
    display: flex; align-items: flex-start; gap: 8px;
    font-size: 14px; line-height: 18px; letter-spacing: 1px; color: var(--white); text-transform: uppercase;
  }
  .brand-mark { width: 12px; height: 12px; margin-top: 3px; background: var(--red); flex: none; }
  .brand-name { display: block; width: 110px; }
  .main-nav { position: absolute; top: 0; left: 0; width: 1020px; height: 70px; z-index: 4; }
  .main-nav a {
    position: absolute; top: 31px; color: var(--white); text-decoration: none;
    font-size: 13px; letter-spacing: 0.6px; white-space: nowrap;
  }
  .main-nav .nav-home { left: 200px; }
  .main-nav .nav-about { left: 307px; }
  .main-nav .nav-services { left: 416px; }
  .main-nav .nav-careers { left: 602px; }
  .main-nav .nav-quote { left: 728px; }
  .main-nav .nav-contact { left: 883px; }

  .hero-photo {
    position: absolute; left: 0; top: 103px; width: 1020px; height: 487px;
    background:
      radial-gradient(ellipse at 55% 55%, rgba(200,200,200,0.35), transparent 55%),
      linear-gradient(#b9b5a8 0%, #7b776c 30%, #3c3b36 60%, #1d1d1b 100%);
  }
  .hero-title {
    position: absolute; left: 180px; top: 208px; width: 645px; height: 114px;
    background: rgba(20,20,20,0.55); text-align: center; padding-left: 32px;
  }
  .hero-title .welcome { display: block; margin-top: 14px; font-size: 24px; line-height: 28px; letter-spacing: 2px; }
  .hero-title .rule { display: block; width: 450px; height: 1px; margin: 3px auto 0; background: rgba(255,255,255,0.25); }
  .hero-title .name { display: block; font-size: 42px; letter-spacing: 0.5px; line-height: 50px; white-space: nowrap; }
  .hero-title .name-blue { color: var(--blue); }
  .hero-title .name-red { color: var(--red); }

  .lower-ground { position: absolute; left: 0; top: 590px; width: 1020px; height: 313px; background: #1a1a1a; }
  .services-panel {
    position: absolute; left: 42px; top: 490px; width: 936px; height: 413px;
    background: linear-gradient(#232323, #1a1a1a); border: 1px solid #2c2c2c;
  }
  .services-panel .panel-top { height: 34px; background: var(--panel-top); border-bottom: 1px solid #2e2e2e; }

  .service-card { position: absolute; top: 553px; width: 261px; }
  .service-card.tilt { left: 70px; }
  .service-card.heavy { left: 377px; }
  .service-card.recovery { left: 690px; }
  .service-card h2 {
    height: 37px; padding: 12px 0 0 15px; font-weight: normal; font-size: 15px; line-height: 18px; letter-spacing: 1.5px;
    background: linear-gradient(#304f95, #13265e); border: 1px solid #46629f;
  }
  .service-photo { height: 152px; }
  .tilt .service-photo { background: linear-gradient(#5f8fd0 0%, #c9d4dc 40%, #7c8c6a 62%, #6e6e6a 100%); }
  .heavy .service-photo { background: linear-gradient(#5c8ee0 0%, #9cbbe6 45%, #8e8d7c 62%, #b7ada2 100%); }
  .recovery .service-photo { background: linear-gradient(#e6e8ea 0%, #b8bdb2 40%, #6f7850 65%, #4f5a35 100%); }
  .service-card p { margin-top: 6px; margin-left: -2px; font-size: 11px; line-height: 16px; letter-spacing: 1px; color: var(--text-soft); }
  .read-more {
    display: block; width: 107px; height: 24px; margin-top: 9px; margin-left: -2px;
    background: linear-gradient(#2e4d94, #142a68); border: 1px solid #3b5ba3;
    color: var(--white); text-decoration: none; font-size: 12px; letter-spacing: 1px; text-align: center; line-height: 22px;
  }

  .about-area { position: absolute; left: 0; top: 903px; width: 1020px; height: 267px; background: linear-gradient(#161616, #000); }
  .about-visual { position: absolute; left: 109px; top: 962px; width: 287px; height: 149px; background: #3a3a3a; padding: 7px; }
  .about-visual .about-photo {
    width: 100%; height: 100%;
    background: linear-gradient(#8a8a8a 0%, #5e5e5e 50%, #2c2c2c 100%);
    display: flex; align-items: center; justify-content: center;
  }
  .about-visual .about-name { font-size: 22px; letter-spacing: 1px; color: var(--white); text-transform: uppercase; white-space: nowrap; }
  .about-copy { position: absolute; left: 436px; top: 967px; width: 468px; }
  .about-copy h2 { font-weight: normal; font-size: 16px; line-height: 20px; letter-spacing: 1.5px; }
  .about-copy p { margin-top: 3px; font-size: 13px; line-height: 23px; letter-spacing: 1px; color: #e6e6e6; }

  .site-footer {
    position: absolute; left: 0; top: 1170px; width: 1020px; height: 30px; background: var(--navy);
    font-size: 10px; letter-spacing: 1px; line-height: 30px;
  }
  .footer-links { position: absolute; left: 78px; }
  .footer-links a { color: var(--white); text-decoration: none; }
  .footer-links span { margin: 0 9px; }
  .copyright { position: absolute; right: 66px; }
</style>
</head>
<body>
  <header class="site-header">
    <div class="brand"><span class="brand-mark"></span><span class="brand-name">Broadway Haulage</span></div>
    <nav class="main-nav">
      <a class="nav-home" href="#">HOME</a>
      <a class="nav-about" href="#">ABOUT</a>
      <a class="nav-services" href="#">TOWING SERVICES</a>
      <a class="nav-careers" href="#">CAREERS</a>
      <a class="nav-quote" href="#">GET A QUOTE</a>
      <a class="nav-contact" href="#">CONTACT</a>
    </nav>
  </header>
  <div class="red-band"></div>

  <section class="hero">
    <div class="hero-photo" role="img" aria-label="Tilt tray tow truck carrying a pickup on a mountain road"></div>
    <div class="hero-title">
      <span class="welcome">WELCOME TO</span>
      <span class="rule"></span>
      <span class="name"><span class="name-blue">BROADWAY</span> <span class="name-red">HAULAGE</span></span>
      <span class="rule"></span>
    </div>
  </section>

  <div class="lower-ground"></div>
  <section class="services-panel"><div class="panel-top"></div></section>

  <article class="service-card tilt">
    <h2>TILT TRAY</h2>
    <div class="service-photo" role="img" aria-label="Tilt tray truck loading a vehicle"></div>
    <p>Lorem ipsum dolor sit amet, consectetur adipiscing elit. Cras ultrices sem tristique, gravida magna a, mattis enim, vivamus</p>
    <a class="read-more" href="#">Read more</a>
  </article>
  <article class="service-card heavy">
    <h2>HEAVY TOWING</h2>
    <div class="service-photo" role="img" aria-label="Heavy tow truck towing a semi truck"></div>
    <p>Lorem ipsum dolor sit amet, consectetur adipiscing elit. Cras ultrices sem tristique, gravida magna a, mattis enim, vivamus</p>
    <a class="read-more" href="#">Read more</a>
  </article>
  <article class="service-card recovery">
    <h2>RECOVERY SPECIALIST</h2>
    <div class="service-photo" role="img" aria-label="Recovery trucks uprighting an overturned trailer"></div>
    <p>Lorem ipsum dolor sit amet, consectetur adipiscing elit. Cras ultrices sem tristique, gravida magna a, mattis enim, vivamus</p>
    <a class="read-more" href="#">Read more</a>
  </article>

  <section class="about-area"></section>
  <div class="about-visual">
    <div class="about-photo" role="img" aria-label="Company truck fleet in greyscale">
      <span class="about-name">Broadway Haulage</span>
    </div>
  </div>
  <div class="about-copy">
    <h2>ABOUT US</h2>
    <p>Lorem ipsum dolor sit amet, consectetur adipiscing elit. Nam lobortis dolor cursus nisl suscipit convallis. Fusce cursus velit at nisl fringilla commodo. Aenean semper odio orci, vel consequat metus euismod at. Phasellus porttitor ipsum sapien, vitae lacinia sem ultricies ut. Fusce tincidunt nisi non sem mattis, at rhoncus mauris dictum.</p>
  </div>

  <footer class="site-footer">
    <div class="footer-links">
      <a href="#">FAQ</a><span>/</span><a href="#">Sitemap</a><span>/</span><a href="#">Product Information</a><span>/</span><a href="#">Customer Service</a>
    </div>
    <div class="copyright">Copyright © 2014 Broadway Haulage</div>
  </footer>
</body>
</html>
```